Now Leasing Banner

Looking for a banner that says the following information approx 4' x 30'

Now Leasing Maplewood Terrace 925-318-6054

Target Market(s)

Drive by traffic

Industry/Entity Type

Residential property management

Requirements
Must have
• Clear and readable from a distance

```html
<!DOCTYPE html>
<html lang="en">
<head>
<meta charset="utf-8">
<title>Now Leasing Banner</title>
<link href="https://fonts.googleapis.com/css2?family=Barlow+Condensed:wght@500;700&display=swap" rel="stylesheet">
<style>
  :root {
    --page-bg: #ffffff;
    --banner-blue: #2357aa;
    --banner-navy: #133a7a;
    --banner-text: #ffffff;
  }
  html, body {
    margin: 0;
    padding: 0;
    width: 1200px;
    height: 1200px;
    overflow: hidden;
    background: var(--page-bg);
  }
  .canvas {
    position: relative;
    width: 1200px;
    height: 1200px;
  }
  .banner {
    position: absolute;
    left: 82px;
    top: 531px;
    width: 1036px;
    height: 137px;
    display: flex;
    box-shadow: 4px 6px 10px rgba(0, 0, 0, 0.35);
  }
  .banner-headline {
    width: 693px;
    height: 137px;
    background: var(--banner-blue);
  }
  .banner-phone {
    width: 343px;
    height: 137px;
    background: var(--banner-navy);
  }
  .banner svg {
    display: block;
    width: 100%;
    height: 100%;
  }
  .headline-text {
    font-family: "Barlow Condensed", "Arial Narrow", sans-serif;
    font-weight: 700;
    font-size: 64px;
    fill: var(--banner-text);
  }
  .phone-text {
    font-family: "Barlow Condensed", "Arial Narrow", sans-serif;
    font-weight: 500;
    font-size: 64px;
    fill: var(--banner-text);
  }
</style>
</head>
<body>
  <div class="canvas">
    <div class="banner">
      <div class="banner-headline">
        <svg viewBox="0 0 693 137" xmlns="http://www.w3.org/2000/svg">
          <text class="headline-text" x="38" y="91" textLength="623" lengthAdjust="spacingAndGlyphs">NOW LEASING MAPLEWOOD TERRACE</text>
        </svg>
      </div>
      <div class="banner-phone">
        <svg viewBox="0 0 343 137" xmlns="http://www.w3.org/2000/svg">
          <text class="phone-text" x="33" y="91" textLength="274" lengthAdjust="spacingAndGlyphs">925-318-6054</text>
        </svg>
      </div>
    </div>
  </div>
</body>
</html>
```